QM Regulatory Pathways - Biz Card - Re-do

I would like a re-do on my business card.

See my Internet site - qmregpathways.example

1) Remove direct phone line.
2) Add company moto - integrity, diligence, and excellence
3) Add Consulting Services listing:
-Benefit Technology
-ERISA Compliance
-Contract/Vendor Management
-Human Resource/Payroll
-Medical/Prescription Drug
-Integrated Leave of Absence

Target Market(s)

Employee benefit consulting and insurance purchasers, Usually human resource executives

Industry/Entity Type

Human Resource

Contact Information for Business Card

Same business card color scheme, logo,

Font styles to use
Sans Serif

Requirements
Must have
• Same color scheme and logo. Remove direct phone number. Keep all numbers, internet address.

```html
<!DOCTYPE html>
<html lang="en">
<head>
<meta charset="utf-8">
<title>QM Regulatory Pathways – Business Card</title>
<link rel="stylesheet" href="https://fonts.googleapis.com/css2?family=Arimo:wght@400&family=Questrial&display=swap">
<style>
  :root {
    --backdrop: #000000;
    --card: #ffffff;
    --plum: #6b1d45;
    --slate: #63666a;
    --on-plum: #ffffff;
  }
  * { margin: 0; padding: 0; box-sizing: border-box; }
  html, body { width: 1019px; height: 1200px; overflow: hidden; background: var(--backdrop); }
  body { position: relative; font-family: "Arimo", Arial, sans-serif; color: var(--slate); }
  .card { position: absolute; background: var(--card); }
  .card-front { left: 69px; top: 100px; width: 877px; height: 500px; }
  .card-back  { left: 76px; top: 631px; width: 877px; height: 501px; }
  .brand-dot { position: absolute; border-radius: 50%; background: var(--plum); }
  .card-front .brand-dot { left: 99px; top: 147px; width: 226px; height: 226px; }
  .card-back .brand-dot  { left: 631px; top: 10px; width: 204px; height: 204px; }
  .brand-name {
    position: absolute; left: 366px; top: 186px;
    font-size: 58px; line-height: 74px; color: var(--slate); white-space: nowrap;
  }
  .motto {
    position: absolute; left: 0; width: 100%; top: 459px;
    text-align: center; font-size: 22px; color: var(--slate);
  }
  .motto .sep { color: var(--slate); padding: 0 2px; }
  .person { position: absolute; left: 26px; top: 27px; font-size: 29px; line-height: 35px; }
  .person-name { color: var(--plum); }
  .person-title { color: var(--slate); }
  .address { position: absolute; left: 26px; top: 120px; font-size: 24px; line-height: 31.5px; }
  .phone-list { position: absolute; left: 29px; top: 246px; }
  .phone-row { display: flex; align-items: baseline; height: 45px; }
  .phone-label { font-family: "Questrial", sans-serif; font-size: 20px; width: 80px; }
  .phone-number { font-size: 25px; }
  .divider { position: absolute; left: 353px; top: 246px; width: 4px; height: 66px; background: var(--plum); }
  .web-list { position: absolute; left: 425px; top: 246px; }
  .web-site { font-size: 25px; line-height: 45px; color: var(--plum); }
  .web-email { font-size: 24px; line-height: 36px; color: var(--slate); }
  .services-heading {
    position: absolute; left: 0; width: 100%; top: 356px;
    display: flex; justify-content: center; align-items: center; gap: 8px;
    font-size: 17px; color: #222;
  }
  .services-heading::before, .services-heading::after {
    content: ""; width: 22px; height: 3px; background: #333;
  }
  .services-band {
    position: absolute; left: 38px; top: 376px; width: 805px; height: 110px;
    background: var(--plum); color: var(--on-plum); font-size: 19px; line-height: 22px;
  }
  .service { position: absolute; white-space: nowrap; }
  .service::before { content: "•"; margin-right: 3px; }
  .service.two-line { text-align: center; }
  .service.two-line::before { content: none; }
</style>
</head>
<body>
  <section class="card card-front">
    <div class="brand-dot"></div>
    <div class="brand-name">QM Regulatory<br>Pathways</div>
    <p class="motto">Integrity<span class="sep">•</span>Diligence<span class="sep">•</span>Excellence</p>
  </section>

  <section class="card card-back">
    <div class="person">
      <div class="person-name">Daniel Hartwell</div>
      <div class="person-title">President</div>
    </div>
    <div class="address">
      418 Larkfield Street,<br>Suite 210<br>Easton, PA 18042
    </div>
    <div class="phone-list">
      <div class="phone-row"><span class="phone-label">Main</span><span class="phone-number">555.014.2730</span></div>
      <div class="phone-row"><span class="phone-label">Fax</span><span class="phone-number">555.014.2731</span></div>
    </div>
    <div class="divider"></div>
    <div class="web-list">
      <div class="web-site">qmregpathways.example</div>
      <div class="web-email">dhartwell@qmregpathways.example</div>
    </div>
    <div class="brand-dot"></div>

    <div class="services-heading">CONSULTING SERVICES</div>
    <div class="services-band">
      <div class="service" style="left:15px; top:10px;">Benefit Technology</div>
      <div class="service" style="left:302px; top:10px;">ERISA Compliance</div>
      <div class="service" style="left:575px; top:10px;">Contract/Vendor Mgt</div>
      <div class="service two-line" style="left:13px; top:55px;">•Human Resource<br>&nbsp;&nbsp;&nbsp;&nbsp;/Payroll</div>
      <div class="service two-line" style="left:285px; top:55px;">•Medical/Prescription<br>Drug</div>
      <div class="service two-line" style="left:571px; top:55px;">•Integrated Leave of<br>Absence</div>
    </div>
  </section>
</body>
</html>
```